Business card (AI file uploaded)

We need a business card design that is minimalist using existing logo (attached). Source files must be editable so we can make the same design with other names.

Screenshots included of a design I was working on to give you an idea of the style I would like. Looking for similar modern styles

Thanks

```html
<!DOCTYPE html>
<html lang="en">
<head>
<meta charset="utf-8">
<title>Halvorsen Law Group – Business Card</title>
<link rel="stylesheet" href="https://fonts.googleapis.com/css2?family=Montserrat:wght@700&family=Questrial&display=swap">
<style>
  :root {
    --page-bg: #d9d6d1;
    --card-black: #0d0d0d;
    --card-black-soft: #262626;
    --card-light: #eeeeee;
    --card-light-edge: #dcdcdc;
    --brand-red: #e0122f;
    --ink-dark: #1f1f1f;
    --ink-white: #ffffff;
    --card-shadow: 0 14px 30px rgba(0,0,0,.28);
  }
  * { margin: 0; padding: 0; box-sizing: border-box; }
  html, body { width: 1200px; height: 900px; overflow: hidden; }
  body {
    background: var(--page-bg);
    font-family: "Questrial", "Century Gothic", sans-serif;
    position: relative;
  }
  .card {
    position: absolute;
    left: 285px;
    width: 630px;
    height: 360px;
    overflow: hidden;
    box-shadow: var(--card-shadow);
  }
  .card--back { top: 60px; }
  .card--front { top: 480px; background: var(--card-light); }

  .texture {
    position: absolute;
    inset: 0;
    background: radial-gradient(ellipse at 55% 40%, var(--card-black-soft) 0%, var(--card-black) 75%);
  }
  .card--front .texture { bottom: auto; height: 186px; }

  .brand {
    position: absolute;
    display: flex;
    align-items: center;
    gap: 16px;
    color: var(--ink-white);
  }
  .brand__dot {
    width: 46px; height: 46px;
    border-radius: 50%;
    background: var(--brand-red);
    flex: none;
  }
  .brand__name {
    font-family: "Questrial", "Century Gothic", sans-serif;
    font-weight: 400;
    letter-spacing: 2px;
    white-space: nowrap;
  }
  .card--back .brand { left: 0; right: 0; top: 130px; justify-content: center; }
  .card--back .brand__name { font-size: 34px; }
  .card--front .brand { right: 40px; top: 70px; }
  .card--front .brand__dot { width: 38px; height: 38px; }
  .card--front .brand__name { font-size: 26px; }

  .services {
    position: absolute;
    left: 0; right: 0; bottom: 34px;
    text-align: center;
    color: var(--ink-white);
    font-size: 14px;
    letter-spacing: .5px;
  }
  .services .sep { color: var(--brand-red); margin: 0 8px; }

  .divider {
    position: absolute;
    left: 0; right: 0; top: 194px;
    height: 2px;
    background: var(--brand-red);
  }
  .light-panel {
    position: absolute;
    left: 0; right: 0; top: 196px; bottom: 0;
    background: linear-gradient(180deg, var(--card-light) 0%, var(--card-light-edge) 100%);
  }

  .holder {
    position: absolute;
    left: 36px; top: 212px;
    font-family: "Montserrat", sans-serif;
    font-weight: 700;
    font-size: 30px;
    letter-spacing: 1px;
    color: var(--ink-dark);
  }
  .holder__last { color: var(--brand-red); }

  .online {
    position: absolute;
    right: 36px; top: 212px;
    text-align: right;
    font-size: 16px;
    line-height: 22px;
    color: var(--ink-dark);
  }
  .contact {
    position: absolute;
    left: 36px; top: 262px;
    list-style: none;
    font-size: 19px;
    line-height: 28px;
    color: var(--ink-dark);
  }
  .contact li { display: flex; align-items: center; gap: 10px; }
  .contact svg { width: 16px; height: 16px; fill: var(--ink-dark); flex: none; }
</style>
</head>
<body>

<section class="card card--back" aria-label="Business card back">
  <div class="texture" role="img" aria-label="Dark square tile texture background"></div>
  <div class="brand">
    <span class="brand__dot"></span>
    <span class="brand__name">HALVORSEN LAW GROUP PC</span>
  </div>
  <p class="services">Real Estate<span class="sep">●</span>Bankruptcy<span class="sep">●</span>Social Security Disability</p>
</section>

<section class="card card--front" aria-label="Business card front">
  <div class="texture" role="img" aria-label="Dark square tile texture background"></div>
  <div class="brand">
    <span class="brand__dot"></span>
    <span class="brand__name">HALVORSEN LAW GROUP PC</span>
  </div>
  <div class="light-panel"></div>
  <div class="divider"></div>

  <h1 class="holder">MARIN <span class="holder__last">HALVORSEN</span></h1>

  <p class="online">HalvorsenLaw.com<br>Marin@HalvorsenLaw.com</p>

  <ul class="contact">
    <li>
      <svg viewBox="0 0 16 16" aria-label="Phone"><path d="M3.6 1.2 6 3.6 4.7 5.4c.8 1.9 2.1 3.2 4 4l1.8-1.3 2.4 2.4-1.6 2.4C6.2 12.6 3.4 9.8 1.2 4.8z"/></svg>
      555 214 7730
    </li>
    <li>
      <svg viewBox="0 0 16 16" aria-label="Fax"><path d="M4 1h6l2 2v3H4zM2 6h12a1 1 0 0 1 1 1v6H1V7a1 1 0 0 1 1-1zm2 4v4h8v-4z"/></svg>
      555 214 7731
    </li>
    <li>410 Meridian Ave. Suite 200, Fairbrook IL 60999</li>
  </ul>
</section>

</body>
</html>
```